Business Card for Technology Startup

Design a 2-sided business card using the logo provided. We are a digital healthcare platform that provides a mobile app and web UI that helps caregivers, families, and doctors share information and provide better patient outcomes. We use AI and machine learning to help guide patients through their day-to-day life. The final design should communicate stability, peace, comfort, but also align with the image of an AI-driven technology startup.

I'd like the deliverable to by a Photoshop PSD file (with layers) that I can work with in pixlr.com. Should contain the following editable layers:
Name (ex. John Doe)
Title (ex. Founder / CEO)
Email (ex. info@brenvaxa.ai)
Phone (ex. (555) 214-8830)
Website (ex. https://brenvaxa.ai)

```html
<!DOCTYPE html>
<html lang="en">
<head>
<meta charset="utf-8">
<title>Brenvaxa – Business Card</title>
<link rel="stylesheet" href="https://fonts.googleapis.com/css2?family=Montserrat:wght@400;600;800&display=swap">
<style>
  :root {
    --page-bg: #2b2b2b;
    --card-bg: #161616;
    --card-back-bg: #1b1b1b;
    --pattern-light: #8a8a8a;
    --pattern-mid: #3a3a3a;
    --pattern-dark: #0c0c0c;
    --brand-blue: #29b6e8;
    --text-white: #ffffff;
    --text-soft: #d6d6d6;
  }
  * { box-sizing: border-box; margin: 0; padding: 0; }
  html, body {
    width: 1200px;
    height: 875px;
    overflow: hidden;
    background: var(--page-bg);
    font-family: "Montserrat", sans-serif;
  }
  .sheet {
    width: 1200px;
    height: 875px;
    display: flex;
    align-items: center;
    justify-content: center;
    gap: 30px;
  }
  .card {
    position: relative;
    width: 560px;
    height: 320px;
    border-radius: 18px;
    overflow: hidden;
    box-shadow: 0 20px 40px rgba(0,0,0,0.45);
  }

  /* Front side */
  .card-front { background: var(--card-bg); }
  .front-texture {
    position: absolute;
    inset: 0;
    background:
      radial-gradient(ellipse at 10% 80%, var(--pattern-light) 0%, var(--pattern-mid) 35%, transparent 65%),
      linear-gradient(135deg, var(--pattern-mid) 0%, var(--pattern-dark) 60%, #050505 100%);
    opacity: 0.85;
  }
  .front-brand {
    position: absolute;
    left: 70px;
    top: 50%;
    transform: translateY(-50%);
    display: flex;
    align-items: center;
    gap: 16px;
  }

  /* Shared brand lockup */
  .brand-dot {
    display: block;
    border-radius: 50%;
    background: var(--brand-blue);
  }
  .brand-name {
    font-weight: 800;
    color: var(--text-white);
    letter-spacing: 0.5px;
    line-height: 1;
  }
  .front-brand .brand-dot { width: 34px; height: 34px; }
  .front-brand .brand-name { font-size: 62px; }

  /* Back side */
  .card-back { background: var(--card-back-bg); }
  .back-brand {
    position: absolute;
    left: 44px;
    top: 56px;
    display: flex;
    align-items: center;
    gap: 12px;
  }
  .back-brand .brand-dot { width: 24px; height: 24px; }
  .back-brand .brand-name { font-size: 44px; }

  .contact-block {
    position: absolute;
    left: 70px;
    top: 156px;
  }
  .person-name {
    font-size: 22px;
    font-weight: 800;
    color: var(--text-white);
  }
  .person-name .first { color: var(--brand-blue); }
  .person-title {
    font-size: 12px;
    font-weight: 400;
    color: var(--text-soft);
    margin-top: 3px;
  }
  .contact-list {
    list-style: none;
    margin-top: 20px;
    display: flex;
    flex-direction: column;
    gap: 8px;
  }
  .contact-item {
    display: flex;
    align-items: center;
    gap: 10px;
    font-size: 12px;
    color: var(--text-soft);
  }
  .contact-icon { width: 14px; height: 14px; flex: none; }
  .contact-icon * { fill: none; stroke: var(--brand-blue); stroke-width: 1.8; stroke-linecap: round; stroke-linejoin: round; }
</style>
</head>
<body>
<main class="sheet">

  <section class="card card-front" aria-label="Card front">
    <div class="front-texture" role="img" aria-label="Dark embossed pattern of rounded connected dots, lit from the lower left"></div>
    <div class="front-brand">
      <span class="brand-dot"></span>
      <span class="brand-name">brenvaxa</span>
    </div>
  </section>

  <section class="card card-back" aria-label="Card back">
    <div class="back-brand">
      <span class="brand-dot"></span>
      <span class="brand-name">brenvaxa</span>
    </div>

    <div class="contact-block">
      <p class="person-name"><span class="first">John</span> Doe</p>
      <p class="person-title">Founder / CEO)</p>

      <ul class="contact-list">
        <li class="contact-item">
          <svg class="contact-icon" viewBox="0 0 16 16" aria-hidden="true">
            <path d="M3 2h3l1.5 3.5-2 1.2a8 8 0 0 0 3.8 3.8l1.2-2L14 10v3a1 1 0 0 1-1 1A11 11 0 0 1 2 3a1 1 0 0 1 1-1z"/>
          </svg>
          <span>(555) 214-8830</span>
        </li>
        <li class="contact-item">
          <svg class="contact-icon" viewBox="0 0 16 16" aria-hidden="true">
            <rect x="1.5" y="3.5" width="13" height="9" rx="1"/>
            <path d="M1.5 4l6.5 5 6.5-5"/>
          </svg>
          <span>info@brenvaxa.ai</span>
        </li>
        <li class="contact-item">
          <svg class="contact-icon" viewBox="0 0 16 16" aria-hidden="true">
            <circle cx="8" cy="8" r="6.5"/>
            <path d="M1.5 8h13M8 1.5c2 2 2 11 0 13M8 1.5c-2 2-2 11 0 13"/>
          </svg>
          <span>https://brenvaxa.ai</span>
        </li>
      </ul>
    </div>
  </section>

</main>
</body>
</html>
```